Street Light Box

We need a New Illuminated light Box Sign. See size in attached document and pics of current sign.
The light box needs to contain "The Harbourview Motel"and then in one third of the box at the bottom promote the restaurant on site. I want white text on black without the logo. Harbourview to be prominent word with elongated text to maximise text size for maximum visibility from a distance.

Target Market(s)

Catch attention of motel

Industry/Entity Type

Motel accommodation

Logo Text

The Harbourview Motel and below Morikawa Grillhouse Restaurant

Logo styles of interest
Wordmark Logo
Lettermark Logo
Font styles to use
Sans Serif

Colors

Designer to choose only greyscale colors for use in the design.

Requirements
Must have
• Fit in Light Box
Nice to have
• Make Harbourview the Champion work with Elongated thick Text

```html
<!DOCTYPE html>
<html lang="en">
<head>
<meta charset="utf-8">
<title>The Harbourview Motel – Street Light Box</title>
<link rel="stylesheet" href="https://fonts.googleapis.com/css2?family=Bebas+Neue&family=Open+Sans:wght@400&family=Roboto:wght@500;900&display=swap">
<style>
  :root {
    --ink: #000000;
    --paper: #ffffff;
    --dimension: #333333;
  }
  html, body {
    margin: 0;
    padding: 0;
    width: 1200px;
    height: 900px;
    overflow: hidden;
    background: var(--paper);
  }
  .sign-drawing {
    display: block;
    width: 1200px;
    height: 900px;
  }
  .dimension-line { stroke: var(--dimension); stroke-width: 1; fill: none; }
  .dimension-label {
    font-family: "Open Sans", sans-serif;
    font-size: 11px;
    fill: var(--dimension);
  }
  .motel-panel { fill: var(--ink); }
  .restaurant-panel { fill: var(--paper); stroke: var(--ink); stroke-width: 1.5; }
  .rule { stroke: var(--paper); stroke-width: 1.5; }
  .motel-small {
    font-family: "Bebas Neue", sans-serif;
    fill: var(--paper);
  }
  .motel-name {
    font-family: "Bebas Neue", sans-serif;
    font-size: 176px;
    fill: var(--paper);
  }
  .restaurant-name {
    font-family: "Roboto", sans-serif;
    font-weight: 900;
    font-size: 72px;
    fill: var(--ink);
  }
  .restaurant-type {
    font-family: "Roboto", sans-serif;
    font-weight: 500;
    font-size: 31px;
    fill: var(--ink);
  }
</style>
</head>
<body>
<svg class="sign-drawing" viewBox="0 0 1200 900" xmlns="http://www.w3.org/2000/svg" role="img" aria-label="Light box sign: The Harbourview Motel, Morikawa Grillhouse Restaurant">
  <!-- width dimension -->
  <g class="dimension">
    <line class="dimension-line" x1="367" y1="180" x2="841" y2="180"/>
    <line class="dimension-line" x1="367" y1="172" x2="367" y2="188"/>
    <line class="dimension-line" x1="841" y1="172" x2="841" y2="188"/>
    <text class="dimension-label" x="604" y="171" text-anchor="middle">2000mm</text>
  </g>
  <!-- height dimensions -->
  <g class="dimension">
    <line class="dimension-line" x1="331" y1="216" x2="331" y2="691"/>
    <line class="dimension-line" x1="320" y1="216" x2="342" y2="216"/>
    <line class="dimension-line" x1="320" y1="533" x2="342" y2="533"/>
    <line class="dimension-line" x1="320" y1="691" x2="342" y2="691"/>
    <text class="dimension-label" transform="translate(320 374) rotate(-90)" text-anchor="middle">1333.33mm</text>
    <text class="dimension-label" transform="translate(320 612) rotate(-90)" text-anchor="middle">666.66mm</text>
  </g>

  <!-- motel panel -->
  <rect class="motel-panel" x="367" y="216" width="474" height="317"/>
  <line class="rule" x1="387" y1="269" x2="547" y2="269"/>
  <line class="rule" x1="663" y1="269" x2="820" y2="269"/>
  <text class="motel-small" x="605" y="291" font-size="58" text-anchor="middle" letter-spacing="12">THE</text>
  <text class="motel-name" x="394" y="440" textLength="420" lengthAdjust="spacingAndGlyphs">HARBOURVIEW</text>
  <line class="rule" x1="387" y1="480" x2="513" y2="480"/>
  <line class="rule" x1="693" y1="480" x2="820" y2="480"/>
  <text class="motel-small" x="607" y="507" font-size="66" text-anchor="middle" letter-spacing="12">MOTEL</text>

  <!-- restaurant panel -->
  <rect class="restaurant-panel" x="367" y="533" width="474" height="158"/>
  <text class="restaurant-name" x="407" y="620" textLength="397" lengthAdjust="spacingAndGlyphs">MORIKAWA</text>
  <text class="restaurant-type" x="604" y="663" text-anchor="middle">Grillhouse Restaurant</text>
</svg>
</body>
</html>
```